Garlic Farm for Farm Sales/Restaurant sales

Need a professional, but appealing to agriculture world. We are selling 27 kinds of Organic Garlic from a farm in Simla,CO. I have uploaded logo and business information-we are going to need a template, because I will need to use it for four separate people.
-We are trying to appeal to Farm to table restaurants
-As well as growers/farmers

Target Market(s)

Agriculture Sales/Restaurants-Organic

Industry/Entity Type

Agriculture

Contact Information for Business Card

Want it to look more unique then your average brimly ink card- I want it to look amazing

Font styles to use
Sans Serif

Colors
0455a3
ec1f27
fbed22
ffffff

Requirements
Must have
• Just be creative
Nice to have
• Colorful
Should not have
• plain

```html
<!DOCTYPE html>
<html lang="en">
<head>
<meta charset="utf-8">
<title>Summit Ridge Garlic – Business Card</title>
<link href="https://fonts.googleapis.com/css2?family=Open+Sans:wght@400;600;700;800&display=swap" rel="stylesheet">
<style>
  :root {
    --bg: #e9e7e5;
    --card: #ffffff;
    --red: #d9212b;
    --navy: #1f2b5e;
    --blue: #0455a3;
    --yellow: #fbed22;
    --soft-grey: #e4e4e6;
    --ink: #1b1b1b;
  }
  * { box-sizing: border-box; margin: 0; padding: 0; }
  html, body {
    width: 1200px; height: 716px; overflow: hidden;
    background: var(--bg);
    font-family: "Open Sans", Arial, sans-serif;
  }
  .stage {
    width: 1200px; height: 716px;
    display: flex; align-items: center; justify-content: center; gap: 60px;
  }
  .card {
    position: relative;
    width: 525px; height: 300px;
    background: var(--card);
    box-shadow: 0 6px 18px rgba(0,0,0,.18);
    overflow: hidden;
  }
  .card-waves { position: absolute; inset: 0; width: 100%; height: 100%; }
  .brand {
    position: absolute;
    display: flex; align-items: center; gap: 10px;
  }
  .brand-dot {
    width: 34px; height: 34px; border-radius: 50%;
    background: var(--red);
    flex: none;
  }
  .brand-name {
    font-weight: 800; color: var(--navy);
    font-size: 25px; line-height: 1.05; letter-spacing: .2px;
  }
  .card-front .brand { left: 50%; top: 118px; transform: translateX(-50%); }
  .card-back .brand { left: 36px; top: 122px; }
  .card-back .brand-name { font-size: 22px; }
  .divider {
    position: absolute; left: 258px; top: 82px;
    width: 2px; height: 136px; background: var(--ink);
  }
  .contact {
    position: absolute; left: 282px; top: 88px;
    color: var(--ink); font-size: 11.5px; line-height: 1.55;
  }
  .contact-name { font-size: 15px; font-weight: 700; margin-bottom: 6px; }
  .contact-row { display: flex; align-items: center; gap: 7px; }
  .contact-row svg { width: 11px; height: 11px; flex: none; fill: var(--ink); }
  .contact-gap { height: 6px; }
  .follow { font-size: 10px; font-weight: 700; margin-top: 4px; }
  .handle { font-size: 11px; color: var(--blue); font-weight: 600; }
</style>
</head>
<body>
<main class="stage">

  <section class="card card-front" aria-label="Card front">
    <svg class="card-waves" viewBox="0 0 525 300" preserveAspectRatio="none" aria-hidden="true">
      <path d="M0 0 H525 V46 C400 12 200 4 0 24 Z" fill="var(--red)"/>
      <path d="M0 24 C200 4 400 12 525 46" fill="none" stroke="var(--blue)" stroke-width="1.2"/>
      <path d="M0 160 C90 170 120 240 260 262 C360 278 440 272 525 258 V300 H0 Z" fill="var(--soft-grey)"/>
      <path d="M0 160 C90 170 120 240 260 262 C360 278 440 272 525 258" fill="none" stroke="var(--red)" stroke-width="2"/>
    </svg>
    <div class="brand">
      <span class="brand-dot"></span>
      <span class="brand-name">Summit Ridge<br>Garlic</span>
    </div>
  </section>

  <section class="card card-back" aria-label="Card back">
    <svg class="card-waves" viewBox="0 0 525 300" preserveAspectRatio="none" aria-hidden="true">
      <path d="M0 0 H525 V60 C400 20 200 4 0 14 Z" fill="var(--red)"/>
      <path d="M0 14 C200 4 400 20 525 60" fill="none" stroke="var(--blue)" stroke-width="1.2"/>
      <path d="M0 210 C90 214 140 262 280 276 C380 286 450 284 525 278 V300 H0 Z" fill="var(--soft-grey)"/>
      <path d="M0 210 C90 214 140 262 280 276 C380 286 450 284 525 278" fill="none" stroke="var(--red)" stroke-width="2"/>
    </svg>
    <div class="brand">
      <span class="brand-dot"></span>
      <span class="brand-name">Summit Ridge<br>Garlic</span>
    </div>
    <div class="divider"></div>
    <div class="contact">
      <p class="contact-name">Dana Welles</p>
      <p class="contact-row">
        <svg viewBox="0 0 24 24"><path d="M6.6 10.8a15.1 15.1 0 0 0 6.6 6.6l2.2-2.2a1 1 0 0 1 1-.25 11.4 11.4 0 0 0 3.6.57 1 1 0 0 1 1 1V20a1 1 0 0 1-1 1A17 17 0 0 1 3 4a1 1 0 0 1 1-1h3.5a1 1 0 0 1 1 1c0 1.25.2 2.45.57 3.57a1 1 0 0 1-.25 1z"/></svg>
        555-014-2283
      </p>
      <p class="contact-row">
        <svg viewBox="0 0 24 24"><path d="M2 5h20v14H2z M4 7v.5l8 5 8-5V7z" fill-rule="evenodd"/></svg>
        Dana@SRGarlic.com
      </p>
      <div class="contact-gap"></div>
      <p class="contact-row">
        <svg viewBox="0 0 24 24"><circle cx="12" cy="12" r="10" fill="none" stroke="#1b1b1b" stroke-width="2"/><path d="M2 12h20M12 2c3 3 3 17 0 20M12 2c-3 3-3 17 0 20" fill="none" stroke="#1b1b1b" stroke-width="1.6"/></svg>
        SRGarlic.com
      </p>
      <p class="contact-row">
        <svg viewBox="0 0 24 24"><path d="M12 2a7 7 0 0 0-7 7c0 5 7 13 7 13s7-8 7-13a7 7 0 0 0-7-7zm0 9.5A2.5 2.5 0 1 1 12 6.5a2.5 2.5 0 0 1 0 5z"/></svg>
        P.O. Box 48 Larkin, CO 80990
      </p>
      <p class="follow">Follow us</p>
      <p class="handle">@summitridgegarlic</p>
    </div>
  </section>

</main>
</body>
</html>
```